Flyer Design Project

We need a flyer design for our company based in Ontario, Canada called CrateLoop. We rent out plastic reusable moving boxes. Please visit Crateloop.ca to find out more information about our company. We are looking for a creative, clean, and fun flyer design. The flyers purpose is to share with others what services CrateLoop offers as well as how convient our service is while still being cheaper than cardboard boxes.

Industry/Entity Type

Plastic

```html
<!DOCTYPE html>
<html lang="en">
<head>
<meta charset="utf-8">
<title>CrateLoop – Moving Boxes Flyer</title>
<link href="https://fonts.googleapis.com/css2?family=Arimo:wght@400;700&display=swap" rel="stylesheet">
<style>
  :root {
    --paper: #e7e8e9;
    --ink: #231f20;
    --green: #7cb843;
    --white: #ffffff;
  }
  * { box-sizing: border-box; margin: 0; padding: 0; }
  html, body { width: 944px; height: 1200px; overflow: hidden; background: var(--paper); }
  .flyer {
    position: relative;
    width: 944px; height: 1200px;
    background: var(--paper);
    font-family: "Arimo", Arial, sans-serif;
    color: var(--ink);
    overflow: hidden;
  }
  .backdrop { position: absolute; inset: 0; width: 944px; height: 1200px; }
  .brand {
    position: absolute; left: 30px; top: 95px;
    display: flex; align-items: center; gap: 18px;
  }
  .brand-square {
    width: 64px; height: 64px; border-radius: 10px; background: var(--green);
  }
  .brand-name { font-size: 58px; font-weight: 700; letter-spacing: -1px; line-height: 64px; color: var(--ink); }
  .headline {
    position: absolute; right: 30px; top: 77px;
    font-size: 88px; font-weight: 700; letter-spacing: -1px; line-height: 100px;
  }
  .tagline {
    position: absolute; left: 0; right: 0; top: 279px;
    text-align: center; font-size: 34px; font-weight: 700; line-height: 40px;
    text-shadow: 2px 3px 4px rgba(0,0,0,0.35);
  }
  .steps { position: absolute; left: 47px; top: 346px; display: flex; gap: 28px; }
  .step {
    width: 265px; height: 253px; background: var(--green);
    border-radius: 14px; overflow: hidden;
    display: flex; flex-direction: column;
  }
  .step-head {
    height: 74px; display: flex; align-items: center; justify-content: center;
    border-bottom: 5px solid var(--paper);
  }
  .step-icon {
    width: 58px; height: 58px; border-radius: 50%; background: var(--white);
    display: flex; align-items: center; justify-content: center;
  }
  .step-text {
    flex: 1; display: flex; align-items: center; justify-content: center;
    text-align: center; padding: 0 18px;
    font-size: 21px; font-weight: 700; line-height: 29px; color: var(--ink);
  }
  .step-text.loose { line-height: 38px; padding: 0 14px; }
  .intro {
    position: absolute; left: 28px; top: 633px; width: 268px;
    font-size: 27px; font-weight: 700; line-height: 41px;
  }
  .product-photo {
    position: absolute; left: 355px; top: 641px;
    width: 450px; height: 450px; border-radius: 50%;
    background: radial-gradient(circle at 50% 55%, #8fc24d 0%, #7cb843 38%, #dfe6d4 62%, #f2f2ee 100%);
    box-shadow: 0 0 0 3px rgba(255,255,255,0.8), 0 4px 14px rgba(0,0,0,0.18);
  }
  .call {
    position: absolute; right: 28px; top: 1077px; text-align: right;
    font-size: 44px; font-weight: 700; line-height: 52px;
  }
  .web {
    position: absolute; left: 28px; top: 1141px;
    font-size: 36px; font-weight: 700; line-height: 44px;
  }
</style>
</head>
<body>
<main class="flyer">
  <svg class="backdrop" viewBox="0 0 944 1200" aria-hidden="true">
    <polygon points="0,1027 944,617 944,725 0,1097" fill="var(--white)"/>
    <polygon points="0,1097 944,725 944,1200 0,1200" fill="var(--green)"/>
  </svg>

  <div class="brand">
    <span class="brand-square"></span>
    <span class="brand-name">CrateLoop</span>
  </div>
  <h1 class="headline">Moving?</h1>
  <h2 class="tagline">Plastic, stackable, eco-friendly moving boxes</h2>

  <section class="steps">
    <article class="step">
      <div class="step-head">
        <span class="step-icon">
          <svg width="38" height="26" viewBox="0 0 38 26" aria-hidden="true">
            <rect x="1" y="2" width="22" height="16" fill="var(--ink)"/>
            <path d="M24 7h7l5 6v5H24z" fill="var(--ink)"/>
            <circle cx="8" cy="21" r="4" fill="var(--ink)" stroke="#fff" stroke-width="1.5"/>
            <circle cx="30" cy="21" r="4" fill="var(--ink)" stroke="#fff" stroke-width="1.5"/>
          </svg>
        </span>
      </div>
      <p class="step-text">We deliver your moving boxes right to your front door (unless you prefer side door).</p>
    </article>
    <article class="step">
      <div class="step-head">
        <span class="step-icon">
          <svg width="34" height="32" viewBox="0 0 34 32" aria-hidden="true" fill="none" stroke="var(--ink)" stroke-width="2.2" stroke-linejoin="round">
            <path d="M7 12v16h20V12"/>
            <path d="M7 12l10 4 10-4"/>
            <path d="M17 16v12"/>
            <path d="M7 12L2 5l10-2 5 6"/>
            <path d="M27 12l5-7-10-2-5 6"/>
          </svg>
        </span>
      </div>
      <p class="step-text loose">Pack it up! Our<br>boxes protect your<br>belongings and<br>make stacking safe.</p>
    </article>
    <article class="step">
      <div class="step-head">
        <span class="step-icon">
          <svg width="32" height="30" viewBox="0 0 32 30" aria-hidden="true" fill="none" stroke="var(--ink)" stroke-width="2.6" stroke-linejoin="round">
            <path d="M3 14L16 3l13 11"/>
            <path d="M7 11v16h18V11"/>
            <rect x="13" y="18" width="6" height="9" fill="var(--ink)"/>
          </svg>
        </span>
      </div>
      <p class="step-text">Once you're<br>unpacked we'll<br>come by your new<br>home and collect<br>the moving boxes.</p>
    </article>
  </section>

  <p class="intro">CrateLoop is here to simplify you move by providing affordable, top quality and eco-friendly plastic moving boxes.</p>

  <div class="product-photo" role="img" aria-label="Photo of a green lidded plastic CrateLoop moving crate over a faded regional map"></div>

  <p class="call">Call us<br>1-800-555-0147</p>
  <p class="web">Log on : www.crateloop.ca</p>
</main>
</body>
</html>
```